Business Card for Consulting Company

I would need a business card for my consulting company - the company brand and logos are defined and shared as part of this project. The proposed design for the business card can be reused as inspiration for my email signature.

```html
<!DOCTYPE html>
<html lang="en">
<head>
<meta charset="utf-8">
<title>Corvana – Business Card</title>
<link rel="stylesheet" href="https://fonts.googleapis.com/css2?family=Exo+2:wght@600&family=Poppins:wght@400;500&display=swap">
<style>
  :root {
    --teal: #00a59d;
    --teal-deep: #009a92;
    --ink: #2f2f2f;
    --paper: #ffffff;
    --backdrop: #d3d6d8;
  }
  * { margin: 0; padding: 0; box-sizing: border-box; }
  html, body { width: 1200px; height: 928px; overflow: hidden; }
  body {
    background: var(--backdrop);
    position: relative;
    font-family: "Poppins", sans-serif;
  }
  .card {
    position: absolute;
    left: 264px;
    width: 672px;
    height: 384px;
    border-radius: 16px;
    overflow: hidden;
  }
  /* Front side */
  .card-front {
    top: 58px;
    background: var(--teal);
    display: flex;
    align-items: center;
    justify-content: center;
  }
  .brand {
    display: flex;
    align-items: center;
    gap: 16px;
    font-family: "Exo 2", sans-serif;
    font-weight: 600;
    line-height: 1;
  }
  .card-front .brand { color: var(--paper); font-size: 78px; }
  .card-front .brand-dot { width: 34px; height: 34px; background: var(--paper); }
  .brand-dot { border-radius: 50%; flex: none; }

  /* Back side */
  .card-back { top: 486px; background: var(--paper); }
  .contact {
    position: absolute;
    left: 55px;
    top: 118px;
  }
  .person-name {
    font-family: "Exo 2", sans-serif;
    font-weight: 600;
    font-size: 27px;
    color: var(--teal);
    line-height: 1.1;
  }
  .person-role {
    font-size: 15px;
    color: var(--ink);
    letter-spacing: 0.4px;
    margin-top: 4px;
  }
  .contact-list { list-style: none; margin-top: 10px; }
  .contact-list li {
    display: flex;
    align-items: center;
    gap: 5px;
    font-size: 15.5px;
    color: var(--ink);
    height: 26.5px;
    letter-spacing: 0.2px;
  }
  .contact-list li.web { color: var(--teal); font-weight: 500; letter-spacing: 0.8px; }
  .contact-list svg { width: 17px; height: 17px; flex: none; }
  .divider {
    position: absolute;
    left: 338px;
    top: 114px;
    width: 1.5px;
    height: 154px;
    background: var(--ink);
  }
  .card-back .brand {
    position: absolute;
    left: 381px;
    top: 160px;
    color: var(--teal);
    font-size: 48px;
    gap: 12px;
  }
  .card-back .brand-dot { width: 24px; height: 24px; background: var(--ink); }
  .bottom-band {
    position: absolute;
    left: 0;
    bottom: 0;
    width: 672px;
    height: 18px;
  }
</style>
</head>
<body>
  <section class="card card-front" aria-label="Card front">
    <div class="brand"><span class="brand-dot"></span>Corvana</div>
  </section>

  <section class="card card-back" aria-label="Card back">
    <div class="contact">
      <h1 class="person-name">Elodie Marsan</h1>
      <p class="person-role">Founder &amp; CEO</p>
      <ul class="contact-list">
        <li>
          <svg viewBox="0 0 24 24" aria-hidden="true"><path fill="var(--teal)" d="M6.6 10.8a15.1 15.1 0 0 0 6.6 6.6l2.2-2.2c.3-.3.7-.4 1-.2 1.1.4 2.3.6 3.6.6.6 0 1 .4 1 1V20c0 .6-.4 1-1 1A17 17 0 0 1 3 4c0-.6.4-1 1-1h3.5c.6 0 1 .4 1 1 0 1.3.2 2.5.6 3.6.1.3 0 .7-.2 1z"/></svg>
          +41 79 418 27 63
        </li>
        <li>
          <svg viewBox="0 0 24 24" aria-hidden="true"><rect x="2" y="5" width="20" height="14" rx="1.5" fill="var(--teal)"/><path d="M3 6.5l9 6.5 9-6.5" fill="none" stroke="#fff" stroke-width="1.6"/></svg>
          elodie.m@corvana.ch
        </li>
        <li class="web">
          <svg viewBox="0 0 24 24" aria-hidden="true"><circle cx="12" cy="12" r="10" fill="var(--ink)"/><path d="M2 12h20M12 2c3 3 3 17 0 20M12 2c-3 3-3 17 0 20" fill="none" stroke="#fff" stroke-width="1.3"/></svg>
          www.corvana.ch
        </li>
      </ul>
    </div>

    <div class="divider"></div>

    <div class="brand"><span class="brand-dot"></span>Corvana</div>

    <svg class="bottom-band" viewBox="0 0 672 18" preserveAspectRatio="none" aria-hidden="true">
      <polygon points="0,0 534,0 516,18 0,18" fill="var(--teal-deep)"/>
      <polygon points="547,0 672,0 672,18 529,18" fill="var(--ink)"/>
    </svg>
  </section>
</body>
</html>
```